PPT Template for an investment fund to use in their pitchbooks

Our firm is an international investment fund and are seeking a PPT template to use in our pitch book (and subsequent PPTs). We would need a template for a title slide and then subsequent text/info slides. A clean & uncluttered feel is preferred as well as no watermark on slides. Please see our logo attached. The logo color code is #19478d. Font is Gotham-Medium.

Target Market(s)

Sophisticated investors

Industry/Entity Type

Finance

Colors
ffffff
0356a4

```html
<!DOCTYPE html>
<html lang="en">
<head>
<meta charset="utf-8">
<title>Examples of default styles</title>
<link rel="stylesheet" href="https://fonts.googleapis.com/css2?family=Montserrat:wght@500;600&family=Carlito&family=Arimo&display=swap">
<style>
  :root {
    --white: #ffffff;
    --brand-navy: #19478d;
    --brand-blue: #0356a4;
    --facet-mid: #2a62ae;
    --facet-light: #3f78c0;
    --box-fill: #4f81bd;
    --box-edge: #385d8a;
    --ink: #111111;
    --rule: #1a1a1a;
  }
  * { margin: 0; padding: 0; box-sizing: border-box; }
  html, body { width: 1200px; height: 897px; overflow: hidden; background: var(--white); }
  .slide {
    position: relative;
    width: 1200px;
    height: 897px;
    background: var(--white);
    overflow: hidden;
  }
  .backdrop { position: absolute; inset: 0; }
  .brand {
    position: absolute;
    left: 16px;
    top: 96px;
    display: flex;
    align-items: center;
    gap: 8px;
    color: var(--white);
    font-family: "Montserrat", sans-serif;
    font-weight: 600;
    font-size: 14.5px;
    letter-spacing: 0.3px;
    white-space: nowrap;
  }
  .brand-mark { width: 12px; height: 12px; background: var(--white); }
  .title-band {
    position: absolute;
    left: 208px;
    top: 202px;
    width: 942px;
    height: 74px;
    background: var(--brand-navy);
    display: flex;
    align-items: center;
    justify-content: center;
  }
  .title {
    color: var(--white);
    font-family: "Montserrat", sans-serif;
    font-weight: 500;
    font-size: 58px;
    line-height: 1;
    letter-spacing: 0.5px;
  }
  .bullets {
    position: absolute;
    left: 250px;
    top: 292px;
    list-style: none;
    font-family: "Carlito", "Calibri", sans-serif;
    font-size: 26px;
    color: var(--ink);
  }
  .bullets li { position: relative; padding-left: 48px; }
  .bullets li::before {
    content: "";
    position: absolute;
    left: 6px;
    top: 14px;
    width: 7px;
    height: 7px;
    border-radius: 50%;
    background: var(--ink);
  }
  .pointer { position: absolute; left: 706px; top: 306px; }
  .sample-table {
    position: absolute;
    left: 805px;
    top: 305px;
    width: 360px;
    height: 187px;
    border-collapse: collapse;
    border: 3px solid var(--rule);
    font-family: "Arimo", "Arial", sans-serif;
    font-size: 27px;
    color: var(--ink);
  }
  .sample-table td {
    border: 1.5px solid var(--rule);
    width: 50%;
    vertical-align: top;
    padding: 6px 12px;
  }
  .text-box {
    position: absolute;
    top: 542px;
    width: 291px;
    height: 176px;
    background: var(--box-fill);
    border: 2px solid var(--box-edge);
    display: flex;
    align-items: center;
    justify-content: center;
    text-align: center;
    font-family: "Arimo", "Arial", sans-serif;
    font-size: 27px;
    line-height: 1.3;
    color: var(--ink);
  }
  .text-box--plain { left: 310px; }
  .text-box--shadow { left: 760px; box-shadow: 6px 6px 8px rgba(0, 0, 0, 0.28); }
  .footer-band {
    position: absolute;
    left: 0;
    bottom: 0;
    width: 1200px;
    height: 18px;
    background: var(--brand-navy);
  }
</style>
</head>
<body>
<main class="slide">
  <svg class="backdrop" width="1200" height="897" viewBox="0 0 1200 897" aria-hidden="true">
    <polygon points="0,0 1200,0 1200,27 199,190 0,541" fill="var(--brand-blue)"/>
    <polygon points="300,0 650,0 199,190" fill="var(--facet-light)"/>
    <polygon points="650,0 1200,0 1200,27 199,190" fill="var(--facet-mid)"/>
    <polygon points="0,0 300,0 0,541" fill="var(--brand-navy)"/>
  </svg>

  <div class="brand"><span class="brand-mark"></span>KESTREL CLAIMS CAPITAL</div>

  <header class="title-band">
    <h1 class="title">Examples of default styles</h1>
  </header>

  <ul class="bullets">
    <li>Text and lines are like this</li>
  </ul>

  <svg class="pointer" width="66" height="16" viewBox="0 0 66 16" aria-hidden="true">
    <line x1="0" y1="8" x2="58" y2="8" stroke="var(--rule)" stroke-width="1.6"/>
    <polygon points="66,8 54,3 54,13" fill="var(--rule)"/>
  </svg>

  <table class="sample-table">
    <tr><td>Table</td><td></td></tr>
    <tr><td></td><td></td></tr>
  </table>

  <div class="text-box text-box--plain">Text box</div>
  <div class="text-box text-box--shadow">Text box<br>With shadow</div>

  <div class="footer-band"></div>
</main>
</body>
</html>
```